Business Card Design Project : Tidewell Press

In preparation for market launch, Whistler's Tidewell Press require the development of a business card. Tidewell Press is a Community online publishing web portal. We provide the the city of Whistler located in B.C. (Canada) business directories, News, Classified ads, News, Events and blogs etc.

The main focus of the brand is to help local businesses to corporate with their online advertisement and marketing. Meeting our clients face to face is a must (B2B).

Target Market(s)

The target market is B2B customers. Business Owners to Marketing, advertising Managers

Industry/Entity Type

Business

Requirements
Must have
• - The business card will be two sided.
the BACK side will have our logo which consist of (icon, url,slogan) submited. The logo will be middle and centred.

The FRONT side should have company details:

Company Legal Name: FERNDALE TIDEWELL PRESS

Owen Marsk
Director of Sales & Marketing

www.ferndaletidewell.biz
owen@ferndaletidewell.biz

Phone: 555 014 3826
#2817 - 562 E. Harlow Ave.
Vancouver, B.C. K7P2R4 Canada
Nice to have
• - For the "FRONT" side of our business card. You can separate or re-arrange with our logo components (icon, logo,slogan). It does not have to be together.

Also our company legal name is rather long so arrange or organize the name in a way to make it shorter. Your experience and creativity will have to come in play.
Should not have
• should not have other colors beside logo color and black text (2 colors). Also nothing Three dimensional

```html
<!DOCTYPE html>
<html lang="en">
<head>
<meta charset="utf-8">
<title>Tidewell Press – Business Card</title>
<link rel="stylesheet" href="https://fonts.googleapis.com/css2?family=Montserrat:wght@800&family=Open+Sans:wght@400;800&family=Questrial&display=swap">
<style>
  :root {
    --backdrop: #d9d9d9;
    --card: #ffffff;
    --brand-blue: #1e7fcf;
    --ink: #111111;
    --card-shadow: rgba(0, 0, 0, 0.18);
  }
  * { margin: 0; padding: 0; box-sizing: border-box; }
  html, body {
    width: 1200px;
    height: 900px;
    overflow: hidden;
    background: var(--backdrop);
  }
  .canvas {
    position: relative;
    width: 1200px;
    height: 900px;
  }
  .card {
    position: absolute;
    width: 640px;
    height: 366px;
    background: var(--card);
    box-shadow: 0 6px 18px var(--card-shadow);
    color: var(--ink);
  }

  /* Back side: company name, centred */
  .card--back { left: 120px; top: 70px; }
  .card--back .brand-name {
    position: absolute;
    left: 0; right: 0; top: 0; bottom: 0;
    display: flex;
    align-items: center;
    justify-content: center;
    font-family: "Open Sans", sans-serif;
    font-weight: 800;
    font-size: 64px;
    color: var(--brand-blue);
  }

  /* Front side: contact details */
  .card--front { left: 440px; top: 480px; }
  .card--front .brand-name {
    position: absolute;
    right: 28px; top: 24px;
    font-family: "Open Sans", sans-serif;
    font-weight: 800;
    font-size: 36px;
    color: var(--ink);
  }
  .person-name {
    position: absolute;
    left: 210px; top: 100px;
    font-family: "Montserrat", sans-serif;
    font-weight: 800;
    font-size: 40px;
  }
  .person-title {
    position: absolute;
    left: 150px; top: 158px;
    font-family: "Questrial", sans-serif;
    font-size: 28px;
  }
  .contact {
    position: absolute;
    left: 30px; bottom: 40px;
    font-family: "Open Sans", sans-serif;
    font-style: normal;
    font-size: 13px;
    line-height: 1.7;
  }
</style>
</head>
<body>
<main class="canvas">
  <section class="card card--back" aria-label="Card back">
    <p class="brand-name">Tidewell Press</p>
  </section>

  <section class="card card--front" aria-label="Card front">
    <p class="brand-name">Tidewell Press</p>
    <h1 class="person-name">Owen Marsk</h1>
    <p class="person-title">Director of Sales &amp; Marketing</p>
    <address class="contact">
      www.ferndaletidewell.biz • owen@ferndaletidewell.biz • Phone: 555 014 3826<br>
      #2817 - 562 E. Harlow Ave. Vancouver, B.C. K7P2R4 Canada
    </address>
  </section>
</main>
</body>
</html>
```